Creative Alcoholic Beverage Package Design Needed!

We need a packaging design for a new alcoholic beverage, including the brand name. Flavours will include Sangria and Margarita, and future line extensions as well. Package will be a box (see attached dieline and example of a competitive product) in a 3 liter format. The dimensions of the box need to match the dieline, but we can be creative on the printing of the box. The product inside will be of high-quality, so the design needs to match this
Updates

Need extra days to review

Target Market(s)

25 to 40 year old, 70% female, 30% male

Colors

Designer to choose colors to be used in the design.

Requirements
Must have
• Be attractive, colourful, modern
• clearly mention the flavour, and show the components of the flavour (Sangria : red wine and citrus) - Margarita (mexican inspiration, lime, etc.)
• Have a clear "brand name" along with the flavours
• Mention the quantity (3 liters), alcohol level : 10% alc./vol.

```html
<!DOCTYPE html>
<html lang="en">
<head>
<meta charset="utf-8">
<title>Verdelle Margarita – 3 ltr box</title>
<link rel="stylesheet" href="https://fonts.googleapis.com/css2?family=Cormorant+Garamond:wght@400;500;600&family=Oswald:wght@700&display=swap">
<style>
  :root {
    --backdrop: #e9e9ea;
    --green-light: #6f9a36;
    --green-mid: #4f7526;
    --green-deep: #2c4415;
    --green-shadow: #1f3010;
    --gold: #e6dd8c;
    --cream: #f4f1e4;
    --lime: #8fc23a;
    --drink: #e9d37e;
  }
  * { box-sizing: border-box; margin: 0; padding: 0; }
  html, body { width: 1200px; height: 1200px; overflow: hidden; }
  body {
    background: var(--backdrop);
    font-family: "Cormorant Garamond", Georgia, serif;
    color: var(--cream);
    position: relative;
  }
  .package { position: absolute; left: 90px; top: 170px; display: flex; }
  .panel-front, .panel-side {
    position: relative;
    height: 860px;
    background: linear-gradient(180deg, var(--green-light) 0%, var(--green-mid) 45%, var(--green-deep) 80%, var(--green-shadow) 100%);
  }
  .panel-front { width: 660px; }
  .panel-side {
    width: 360px;
    border-left: 1px solid rgba(0,0,0,.25);
    background: linear-gradient(180deg, #5e8a2e 0%, #45682120 0%, #4a6e24 40%, #2a4114 85%, #1f3010 100%);
  }

  .brand-name {
    position: absolute; left: 0; right: 0; top: 120px;
    text-align: center; font-size: 96px; font-weight: 500; color: var(--cream);
    letter-spacing: 1px;
  }
  .photo {
    position: absolute;
    border-radius: 6px;
  }
  .photo-glass {
    left: 30px; top: 300px; width: 440px; height: 420px;
    background: radial-gradient(ellipse at 45% 35%, var(--drink) 0%, #c9bb6a 35%, rgba(120,150,60,.5) 65%, rgba(79,117,38,0) 80%);
  }
  .photo-limes {
    left: 20px; top: 660px; width: 470px; height: 200px;
    background: radial-gradient(ellipse at 60% 55%, var(--lime) 0%, #5f9a26 45%, rgba(44,68,21,0) 75%);
  }
  .flavour {
    position: absolute; left: 400px; top: 505px; width: 250px;
    font-size: 50px; font-weight: 500; color: var(--gold);
  }
  .tagline {
    position: absolute; left: 360px; top: 575px; width: 290px;
    text-align: center; font-size: 31px; line-height: 1.15; color: var(--cream);
  }
  .volume {
    position: absolute; right: 40px; bottom: 30px; text-align: right; color: #fff;
  }
  .volume .amount { font-family: "Oswald", Impact, sans-serif; font-size: 64px; line-height: 1; }
  .volume .unit { font-size: 30px; font-weight: 600; }
  .volume .abv { display: block; font-size: 22px; font-weight: 600; }

  .side-brand { position: absolute; left: 0; right: 0; top: 90px; text-align: center; font-size: 46px; font-weight: 500; }
  .side-flavour { position: absolute; left: 0; right: 0; top: 150px; text-align: center; font-size: 22px; color: var(--gold); }
  .rule { position: absolute; left: 40px; right: 40px; height: 1px; background: rgba(244,241,228,.35); }
  .side-intro {
    position: absolute; left: 40px; right: 40px; top: 210px;
    font-size: 15px; line-height: 1.45; text-align: center;
  }
  .side-band {
    position: absolute; left: 0; right: 0; top: 310px; height: 34px;
    background: linear-gradient(90deg, rgba(230,221,140,.15), rgba(230,221,140,.55), rgba(230,221,140,.15));
    color: var(--green-deep); font-size: 18px; font-weight: 600;
    text-align: center; line-height: 34px;
  }
  .info { position: absolute; width: 200px; font-size: 11px; line-height: 1.35; }
  .info h3 { font-size: 13px; font-weight: 600; color: var(--gold); margin-bottom: 3px; }
  .info-serve { left: 30px; top: 380px; }
  .info-tap { right: 30px; top: 470px; text-align: right; }
  .info-lime { left: 30px; top: 580px; }
  .icon { position: absolute; }
  .icon-glass { right: 40px; top: 372px; }
  .icon-tap { left: 40px; top: 480px; }
  .icon-lime { right: 45px; top: 570px; }
  .tap-outline { position: absolute; left: 60px; top: 640px; }
  .side-abv { position: absolute; right: 40px; bottom: 28px; font-size: 16px; font-weight: 600; }
</style>
</head>
<body>
  <main class="package">
    <section class="panel-front">
      <h1 class="brand-name">Verdelle</h1>
      <div class="photo photo-glass" role="img" aria-label="Photo of a margarita glass with sugared green rim, lime wedge and mint"></div>
      <div class="photo photo-limes" role="img" aria-label="Photo of fresh limes, a halved lime and mint leaves"></div>
      <h2 class="flavour">Margarita</h2>
      <p class="tagline">Mexican Inspiration<br>&amp; Lime</p>
      <p class="volume"><span class="amount">3</span><span class="unit">ltr</span><span class="abv">10% alc.</span></p>
    </section>

    <aside class="panel-side">
      <h2 class="side-brand">Verdelle</h2>
      <p class="side-flavour">Margarita</p>
      <div class="rule" style="top:190px"></div>
      <p class="side-intro">A smooth blend of fresh lime, agave notes and a light salty finish, crafted for sunny evenings with friends.</p>
      <p class="side-band">Mexican Inspiration &amp; Lime</p>

      <svg class="icon icon-glass" width="28" height="36" viewBox="0 0 28 36" fill="none" stroke="var(--gold)" stroke-width="1.8">
        <path d="M2 4 H26 L14 18 Z"/><path d="M14 18 V32 M7 33 H21"/>
      </svg>
      <div class="info info-serve"><h3>Serve chilled</h3><p>Pour over ice and garnish with a lime wedge.</p></div>

      <svg class="icon icon-tap" width="30" height="34" viewBox="0 0 30 34" fill="none" stroke="var(--cream)" stroke-width="1.8">
        <rect x="2" y="3" width="22" height="8" rx="2"/><path d="M10 11 V20 H16 V11"/><path d="M13 24 V30"/>
      </svg>
      <div class="info info-tap"><h3>Easy tap</h3><p>Press the tap gently to pour each glass.</p></div>

      <svg class="icon icon-lime" width="34" height="34" viewBox="0 0 34 34" fill="none" stroke="var(--gold)" stroke-width="1.8">
        <circle cx="17" cy="17" r="14"/><circle cx="17" cy="17" r="9"/><path d="M17 8 V26 M8 17 H26"/>
      </svg>
      <div class="info info-lime"><h3>Fresh lime</h3><p>Made with real lime for a bright taste.</p></div>

      <div class="rule" style="top:660px; opacity:.5"></div>
      <svg class="tap-outline" width="200" height="180" viewBox="0 0 200 180" fill="none" stroke="#b9b7d8" stroke-width="1.2" stroke-dasharray="4 4">
        <path d="M10 0 V130 L60 170 H150 V100 L190 80 V0"/>
      </svg>
      <p class="side-abv">10% alc./vol.</p>
    </aside>
  </main>
</body>
</html>
```